Carver Lindqvist Group Business Cards

We have a new logo, and want to design new business cards with it. We are 21 years in business, and want a fresh but professional look, so not a lot of extra stuff on the card. We are a recruiting and staffing firm focused on placing accounting and finance professionals in the Dallas TX area. I've attached our new logo that should be displayed on the cards. Here is what I think we want on the cards:
Ray Pemberly, CPA
Partner and Managing Director
8282 Orchard Vale Rd.
Suite 610
Dallas, TX 75391
O 214-555-0184
M 214-555-0237
ray@carverlindqvist.example
www.carverlindqvist.example

```html
<!DOCTYPE html>
<html lang="en">
<head>
<meta charset="utf-8">
<title>Carver Lindqvist Group – Business Cards</title>
<link rel="stylesheet" href="https://fonts.googleapis.com/css2?family=Open+Sans:wght@400;600&display=swap">
<style>
  :root {
    --backdrop: #202022;
    --card-dark: #141416;
    --card-light: #ffffff;
    --brand-blue: #2c4a8e;
    --navy: #1f3670;
    --ink-grey: #6a6a6a;
    --text-grey: #5a5a5a;
    --rule-grey: #8a8a8a;
  }
  * { box-sizing: border-box; margin: 0; padding: 0; }
  html, body { width: 1200px; height: 900px; overflow: hidden; }
  body {
    background: var(--backdrop);
    font-family: "Open Sans", Arial, sans-serif;
    position: relative;
  }
  .card {
    position: absolute;
    left: 285px;
    width: 630px;
    height: 360px;
    box-shadow: 0 10px 30px rgba(0,0,0,0.55);
  }
  /* Back of card */
  .card-back {
    top: 70px;
    background: var(--card-dark);
    display: flex;
    flex-direction: column;
    align-items: center;
    justify-content: center;
  }
  .brand-lockup {
    display: flex;
    align-items: center;
    gap: 12px;
  }
  .brand-mark {
    width: 18px;
    height: 18px;
    background: var(--brand-blue);
  }
  .brand-name {
    font-weight: 600;
    color: var(--brand-blue);
    letter-spacing: 0.04em;
    text-transform: uppercase;
  }
  .card-back .brand-name { font-size: 30px; }
  .brand-rule {
    width: 400px;
    height: 2px;
    background: var(--rule-grey);
    opacity: 0.7;
    margin-top: 14px;
  }
  .website {
    margin-top: 34px;
    font-size: 15px;
    font-weight: 600;
    letter-spacing: 0.22em;
    color: var(--brand-blue);
    text-transform: uppercase;
  }
  /* Front of card */
  .card-front {
    top: 470px;
    background: var(--card-light);
  }
  .person {
    position: absolute;
    left: 40px;
    top: 36px;
  }
  .person-name {
    font-size: 24px;
    font-weight: 400;
    color: var(--ink-grey);
    text-transform: uppercase;
    letter-spacing: 0.01em;
  }
  .person-name .credential { font-size: 17px; }
  .person-title {
    margin-top: 4px;
    font-size: 14px;
    font-weight: 400;
    color: var(--navy);
    text-transform: uppercase;
  }
  .title-rule {
    margin-top: 10px;
    width: 86px;
    height: 3px;
    background: var(--navy);
  }
  .card-front .brand-lockup {
    position: absolute;
    right: 36px;
    top: 120px;
    flex-direction: column;
    align-items: flex-end;
    gap: 0;
  }
  .card-front .brand-row {
    display: flex;
    align-items: center;
    gap: 8px;
  }
  .card-front .brand-mark { width: 12px; height: 12px; }
  .card-front .brand-name { font-size: 18px; color: var(--navy); }
  .card-front .brand-rule { width: 250px; height: 1px; margin-top: 8px; }
  .contact {
    position: absolute;
    left: 40px;
    top: 210px;
    font-size: 15px;
    color: var(--text-grey);
    line-height: 24px;
    list-style: none;
  }
  .contact li { display: flex; align-items: center; gap: 10px; }
  .contact svg { width: 14px; height: 14px; fill: none; stroke: var(--navy); stroke-width: 1.6; }
  .contact .icon-solid { fill: var(--navy); stroke: none; }
  .address { position: absolute; left: 40px; top: 290px; font-size: 15px; color: var(--text-grey); line-height: 24px; }
</style>
</head>
<body>
  <section class="card card-back" aria-label="Card back">
    <div class="brand-lockup">
      <span class="brand-mark"></span>
      <span class="brand-name">Carver Lindqvist Group</span>
    </div>
    <div class="brand-rule"></div>
    <p class="website">www.carverlindqvist.example</p>
  </section>

  <section class="card card-front" aria-label="Card front">
    <div class="person">
      <h1 class="person-name">Ray Pemberly, <span class="credential">CPA</span></h1>
      <p class="person-title">Partner and Managing Director</p>
      <div class="title-rule"></div>
    </div>

    <div class="brand-lockup">
      <div class="brand-row">
        <span class="brand-mark"></span>
        <span class="brand-name">Carver Lindqvist Group</span>
      </div>
      <div class="brand-rule"></div>
    </div>

    <ul class="contact">
      <li>
        <svg viewBox="0 0 16 16" aria-hidden="true"><path class="icon-solid" d="M3.5 1.5l2.5 0 1 3.5-1.6 1.2a8 8 0 0 0 4.4 4.4L11 9l3.5 1v2.5c0 1-1 2-2 2A11 11 0 0 1 1.5 3.5c0-1 1-2 2-2z"/></svg>
        214-555-0184
      </li>
      <li>
        <svg viewBox="0 0 16 16" aria-hidden="true"><rect x="1.5" y="3.5" width="13" height="9"/><path d="M1.5 3.5l6.5 5 6.5-5"/></svg>
        214-555-0237
      </li>
      <li>
        <svg viewBox="0 0 16 16" aria-hidden="true"><circle cx="8" cy="8" r="6.5"/><ellipse cx="8" cy="8" rx="3" ry="6.5"/><path d="M1.5 8h13"/></svg>
        ray@carverlindqvist.example
      </li>
    </ul>
    <address class="address" style="font-style: normal;">
      8282 Orchard Vale Rd.<br>
      Suite 610, Dallas, TX 75391
    </address>
  </section>
</body>
</html>
```